Food truck menu design

Looking for a menu to be dissed for my toasted sandwich food truck. I have attached to logo and photo of the food truck for inspiration. if it can tie into them.
needing three sections, with titles:
CLASSICS
- classic one
. description
-Classic two
. Description
PREMIUM
- Premium one
. description
-Premium Two
. Description
-Premium Three
. Description
DESERT
-Desert one
. Description
-Desert two
.Description

also if it can be editable so I can change menu items and descriptions.

```html
<!DOCTYPE html>
<html lang="en">
<head>
<meta charset="utf-8">
<title>Milo's Melts — Menu</title>
<link href="https://fonts.googleapis.com/css2?family=Poppins:ital,wght@0,400;0,600;0,800;1,400&display=swap" rel="stylesheet">
<style>
  :root{
    --orange:#f6a21e;
    --brown:#4a1810;
    --red:#b5373a;
    --white:#ffffff;
    --cream:#fdf8ee;
  }
  html,body{margin:0;padding:0;overflow:hidden;background:var(--white);}
  .canvas{position:relative;width:1200px;height:1200px;background:var(--white);font-family:'Poppins',sans-serif;overflow:hidden;}
  .menu-frame{position:absolute;left:229px;top:74px;width:738px;height:1048px;border:6px solid var(--orange);}
  .pattern-fill{position:absolute;left:235px;top:80px;width:738px;height:1048px;background:linear-gradient(180deg,var(--cream),#fffaf2);}
  .brand{position:absolute;left:235px;top:250px;width:738px;display:flex;justify-content:center;align-items:center;gap:14px;}
  .brand-dot{width:26px;height:26px;border-radius:50%;background:var(--orange);}
  .brand-name{margin:0;font-weight:600;font-size:58px;color:var(--brown);letter-spacing:1px;}
  .ribbon{position:absolute;left:0;top:0;width:1200px;height:1200px;pointer-events:none;}
  .section-title{position:absolute;left:461px;width:285px;height:39px;background:var(--brown);color:var(--white);font-weight:800;font-size:26px;line-height:40px;text-align:center;margin:0;}
  .panel{position:absolute;background:var(--orange);border-radius:10px;}
  .item{position:absolute;width:257px;height:83px;background:var(--white);border-radius:10px;}
  .item-name{position:absolute;left:29px;top:8px;margin:0;font-weight:400;font-size:24px;color:var(--red);white-space:nowrap;}
  .item-name::before{content:"";position:absolute;left:-22px;top:11px;width:14px;height:14px;border-radius:50%;background:var(--red);}
  .item-desc{position:absolute;left:29px;top:41px;margin:0;font-style:italic;font-size:13.5px;line-height:16px;color:var(--brown);width:160px;}
  .price{position:absolute;right:-29px;top:13px;width:56px;height:56px;border-radius:50%;background:var(--red);color:var(--white);font-weight:800;font-size:24px;line-height:56px;text-align:center;}
</style>
</head>
<body>
<div class="canvas">
  <div class="pattern-fill" role="img" aria-label="Faint repeating pattern of toasted sandwich triangles"></div>
  <div class="menu-frame"></div>

  <header class="brand">
    <span class="brand-dot"></span>
    <h1 class="brand-name">Milo's Melts</h1>
  </header>

  <!-- Classics -->
  <div class="panel" style="left:269px;top:511px;width:670px;height:134px;"></div>
  <!-- Premium -->
  <div class="panel" style="left:269px;top:691px;width:670px;height:134px;"></div>
  <div class="panel" style="left:454px;top:810px;width:300px;height:104px;border-radius:0 0 8px 8px;"></div>
  <!-- Desert -->
  <div class="panel" style="left:269px;top:959px;width:670px;height:134px;"></div>

  <svg class="ribbon" viewBox="0 0 1200 1200" aria-hidden="true">
    <g fill="#4a1810">
      <polygon points="424,511 461,511 461,537 478,537 485,550 424,550 444,530"/>
      <polygon points="783,511 746,511 746,537 729,537 722,550 783,550 763,530"/>
      <polygon points="424,691 461,691 461,717 478,717 485,730 424,730 444,710"/>
      <polygon points="783,691 746,691 746,717 729,717 722,730 783,730 763,710"/>
      <polygon points="424,959 461,959 461,985 478,985 485,998 424,998 444,978"/>
      <polygon points="783,959 746,959 746,985 729,985 722,998 783,998 763,978"/>
    </g>
  </svg>

  <h2 class="section-title" style="top:491px;">CLASSICS</h2>
  <h2 class="section-title" style="top:671px;">PREMIUM</h2>
  <h2 class="section-title" style="top:939px;">DESERT</h2>

  <article class="item" style="left:277px;top:556px;">
    <h3 class="item-name">Classic One</h3>
    <p class="item-desc">Lorem ipsum dolor sit amet, consectetuer</p>
    <span class="price">$</span>
  </article>
  <article class="item" style="left:644px;top:556px;">
    <h3 class="item-name">Classic Two</h3>
    <p class="item-desc">Lorem ipsum dolor sit amet, consectetuer</p>
    <span class="price">$</span>
  </article>

  <article class="item" style="left:277px;top:736px;">
    <h3 class="item-name">Premium One</h3>
    <p class="item-desc">Lorem ipsum dolor sit amet, consectetuer</p>
    <span class="price">$</span>
  </article>
  <article class="item" style="left:644px;top:736px;">
    <h3 class="item-name">Premium Two</h3>
    <p class="item-desc">Lorem ipsum dolor sit amet, consectetuer</p>
    <span class="price">$</span>
  </article>
  <article class="item" style="left:461px;top:826px;">
    <h3 class="item-name">Premium Three</h3>
    <p class="item-desc">Lorem ipsum dolor sit amet, consectetuer</p>
    <span class="price">$</span>
  </article>

  <article class="item" style="left:277px;top:1005px;">
    <h3 class="item-name">Desert One</h3>
    <p class="item-desc">Lorem ipsum dolor sit amet, consectetuer</p>
    <span class="price">$</span>
  </article>
  <article class="item" style="left:644px;top:1005px;">
    <h3 class="item-name">Desert Two</h3>
    <p class="item-desc">Lorem ipsum dolor sit amet, consectetuer</p>
    <span class="price">$</span>
  </article>
</div>
</body>
</html>
```